Business card for Eyelash extension salon in Beverly Hills,California USA

We need new business card for our salon in Beverly Hills. The salon name is 'Lumarra' . We would like to have...Business name: Lumarra Name of person: will provide later Address 6128 N.Corbel Ridge Blvd Beverly Hills , CA 90210 Phone: will provide later (Text only) Web: www.lumarrastudio-example.com Pictogrid icon, Friendvale icon follow us for seasonal campaign and news @lumarrastudioexample Design should look elegant, high-end, clean, simple, cohesive with my brand. Please refer my brand board. Business name color will be metallic bronzy color. Im thinking grey background or white background. Thanks

Target Market(s)

25-35. Gender neutral. People who are in Entertainment business industry.
This is High-end Eyelash extension salon in Beverly Hills

Industry/Entity Type

Beauty Salon

Contact Information for Business Card

Business name: Lumarra
Name of person: will provide later
Address 6128 N.Corbel Ridge Blvd Beverly Hills , CA 90210
Phone: will provide later (Text only)
Web: www.lumarrastudio-example.com
Pictogrid icon, Friendvale icon
follow us for seasonal campaign and news @lumarrastudioexample

Requirements
Must have
• Beautiful, elegant, clean and simple look but very attractive and modern
Should not have
• We don't like too clutter, too busy designs.

```html
<!DOCTYPE html>
<html lang="en">
<head>
<meta charset="utf-8">
<title>Lumarra Business Card</title>
<link rel="stylesheet" href="https://fonts.googleapis.com/css2?family=Arimo:wght@700&family=Lato:ital,wght@0,300;0,400;1,700&display=swap">
<style>
  :root {
    --stage: #1b1b1b;
    --card-light: #f3f3f3;
    --card-bronze: #8a6a51;
    --bronze-text: #7a5a43;
    --body-text: #3a3a3a;
    --white: #ffffff;
    --rule: #d9c6b4;
  }
  * { margin: 0; padding: 0; box-sizing: border-box; }
  html, body { width: 1200px; height: 900px; overflow: hidden; background: var(--stage); }
  .canvas { position: relative; width: 1200px; height: 900px; font-family: "Lato", sans-serif; }

  .card { position: absolute; top: 200px; width: 310px; height: 502px; box-shadow: 3px 3px 4px rgba(0,0,0,0.55); }
  .card--front { left: 253px; background: var(--card-light); border-radius: 62px 0 62px 0; }
  .card--back { left: 627px; background: var(--card-bronze); border-radius: 0 62px 0 62px; }

  .brand { position: absolute; left: 0; width: 100%; text-align: center; }
  .brand__name { display: block; font-weight: 300; font-size: 54px; letter-spacing: 1px; line-height: 1; }
  .brand__place { display: block; margin-top: 14px; padding-left: 96px; font-size: 8.5px; letter-spacing: 1.6px; }
  .card--front .brand { top: 128px; color: var(--bronze-text); }
  .card--back .brand { top: 132px; color: var(--white); }

  .contact { position: absolute; left: 33px; top: 344px; color: var(--body-text); font-size: 14px; line-height: 18px; }
  .contact__person { font-family: "Arimo", sans-serif; font-weight: 700; font-size: 18px; color: var(--bronze-text); margin-bottom: 12px; }
  .contact__address { margin-bottom: 12px; }
  .contact__row { display: flex; align-items: center; gap: 4px; }
  .contact__row svg { width: 13px; height: 13px; fill: var(--bronze-text); }

  .social { position: absolute; left: 0; top: 393px; width: 100%; text-align: center; color: var(--white); }
  .social__bar { display: flex; align-items: center; justify-content: center; gap: 6px; height: 20px; }
  .social__rule { width: 72px; height: 1px; background: var(--rule); }
  .social__dot { width: 19px; height: 19px; border-radius: 50%; background: var(--white); }
  .social__note { margin-top: 12px; font-size: 14px; line-height: 18px; }
  .social__handle { font-weight: 700; font-style: italic; }
</style>
</head>
<body>
<main class="canvas">
  <section class="card card--front">
    <div class="brand">
      <span class="brand__name">Lumarra</span>
      <span class="brand__place">BEVERLY HILLS</span>
    </div>
    <div class="contact">
      <p class="contact__person">DANIEL REYES</p>
      <p class="contact__address">6128 N.Corbel Ridge<br>Blvd Beverly Hills , CA 90210</p>
      <p class="contact__row">
        <svg viewBox="0 0 16 16" aria-hidden="true"><path d="M1 6c0-2 3-4 7-4s7 2 7 4v1h-4V5.5H5V7H1zM4 8h8l2 6H2z"/></svg>
        044-555 010 246
      </p>
      <p class="contact__row">
        <svg viewBox="0 0 16 16" aria-hidden="true"><circle cx="8" cy="8" r="7"/></svg>
        www.lumarrastudio-example.com
      </p>
    </div>
  </section>

  <section class="card card--back">
    <div class="brand">
      <span class="brand__name">Lumarra</span>
      <span class="brand__place">BEVERLY HILLS</span>
    </div>
    <div class="social">
      <div class="social__bar">
        <span class="social__rule"></span>
        <span class="social__dot" aria-label="Friendvale"></span>
        <span class="social__dot" aria-label="Pictogrid"></span>
        <span class="social__rule"></span>
      </div>
      <p class="social__note">Follow us for seasonal campaign<br>and news <span class="social__handle">@lumarrastudioexample</span></p>
    </div>
  </section>
</main>
</body>
</html>
```